Property Management Company Business Cards

Need business cards for a property management company located in Michigan. We manage houses for clients all over the world. Young and modern company, looking for eye catching design. Please work with the attached logo.

Industry/Entity Type

Property Management

Requirements
Must have
• Need lines for address, telephone number, fax number, web site.

Also lines for name, and job title

```html
<!DOCTYPE html>
<html lang="en">
<head>
<meta charset="utf-8">
<title>Lakeshore Harbor Homes – Business Cards</title>
<link rel="stylesheet" href="https://fonts.googleapis.com/css2?family=Ubuntu:wght@400;500;700&display=swap">
<style>
  :root {
    --page-bg: #2a2b2d;
    --card-frame: #f4f6f7;
    --steel-blue: #5a7791;
    --mist-blue: #a9c0c9;
    --back-blue: #b6ccd4;
    --night: #1c232c;
    --divider: #e7e1c9;
    --ink-light: #eef3f6;
    --logo-ink: #2b3036;
    --accent-blue: #1d94d2;
  }
  * { box-sizing: border-box; margin: 0; padding: 0; }
  html, body { width: 1200px; height: 900px; overflow: hidden; }
  body {
    background: var(--page-bg);
    font-family: "Ubuntu", "Segoe UI", sans-serif;
    position: relative;
  }
  .card {
    position: absolute;
    left: 250px;
    width: 700px;
    height: 400px;
    background: var(--card-frame);
    padding: 22px;
    box-shadow: 0 10px 30px rgba(0,0,0,.5);
  }
  .card--back { top: 40px; }
  .card--front { top: 460px; }

  .back-face {
    width: 100%; height: 100%;
    background: var(--back-blue);
    display: flex; align-items: center; justify-content: center;
  }

  .brand { display: flex; align-items: center; gap: 14px; }
  .brand-dot {
    width: 34px; height: 34px; border-radius: 50%;
    background: var(--accent-blue);
  }
  .brand-name {
    font-weight: 700; font-size: 34px; letter-spacing: .5px;
    color: var(--logo-ink); text-transform: uppercase;
    white-space: nowrap;
  }

  .front-face {
    width: 100%; height: 100%;
    display: grid;
    grid-template-rows: 164px 3px 92px 1fr;
  }
  .band-info {
    background: var(--steel-blue);
    display: flex; justify-content: space-between; align-items: flex-end;
    padding: 0 28px 26px 26px;
    color: var(--ink-light);
  }
  .person-name { font-size: 26px; font-weight: 700; }
  .person-title { font-size: 17px; margin-top: 6px; }
  .contact-list { list-style: none; align-self: center; padding-top: 4px; }
  .contact-list li {
    display: flex; align-items: center; gap: 16px;
    font-size: 15px; letter-spacing: .4px; margin: 9px 0;
    white-space: nowrap;
  }
  .contact-list svg, .footer-item svg { width: 20px; height: 20px; flex: none; }
  .divider { background: var(--divider); }
  .band-brand {
    background: var(--mist-blue);
    display: flex; align-items: center; justify-content: center;
  }
  .band-footer {
    background: var(--night);
    color: #d9e2e8;
    position: relative;
  }
  .footer-item {
    position: absolute;
    display: flex; align-items: center; gap: 16px;
    font-size: 17px; letter-spacing: .5px;
    white-space: nowrap;
  }
  .footer-item--web { right: 28px; top: 18px; }
  .footer-item--mail { left: 26px; bottom: 18px; }
</style>
</head>
<body>

<section class="card card--back">
  <div class="back-face">
    <div class="brand">
      <span class="brand-dot"></span>
      <span class="brand-name">Lakeshore Harbor Homes</span>
    </div>
  </div>
</section>

<section class="card card--front">
  <div class="front-face">
    <div class="band-info">
      <div class="person">
        <p class="person-name">John Doe</p>
        <p class="person-title">General Manager</p>
      </div>
      <ul class="contact-list">
        <li>
          <svg viewBox="0 0 20 20" fill="none" stroke="#e6edf1" stroke-width="1.6"><rect x="5" y="1.5" width="10" height="17" rx="2"/><line x1="8" y1="15.5" x2="12" y2="15.5"/></svg>
          +1 616-555-0142
        </li>
        <li>
          <svg viewBox="0 0 20 20" fill="none" stroke="#e6edf1" stroke-width="1.6"><rect x="2" y="8" width="16" height="10" rx="1.5"/><rect x="5" y="2" width="10" height="6"/><line x1="6" y1="12" x2="14" y2="12"/><line x1="6" y1="15" x2="14" y2="15"/></svg>
          +1 616-555-0187
        </li>
        <li>
          <svg viewBox="0 0 20 20"><path d="M10 1.5a6 6 0 0 0-6 6c0 4.5 6 11 6 11s6-6.5 6-11a6 6 0 0 0-6-6z" fill="#e6edf1"/><circle cx="10" cy="7.5" r="2.2" fill="#5a7791"/></svg>
          Birchwood Ave. 12, Lakeview, MI
        </li>
      </ul>
    </div>
    <div class="divider"></div>
    <div class="band-brand">
      <div class="brand">
        <span class="brand-dot"></span>
        <span class="brand-name">Lakeshore Harbor Homes</span>
      </div>
    </div>
    <div class="band-footer">
      <p class="footer-item footer-item--web">
        <svg viewBox="0 0 20 20" fill="none" stroke="#cfd9df" stroke-width="1.4"><circle cx="10" cy="10" r="8"/><ellipse cx="10" cy="10" rx="3.5" ry="8"/><line x1="2" y1="10" x2="18" y2="10"/><line x1="3.5" y1="5.5" x2="16.5" y2="5.5"/><line x1="3.5" y1="14.5" x2="16.5" y2="14.5"/></svg>
        www.yourwebsitename.com
      </p>
      <p class="footer-item footer-item--mail">
        <svg viewBox="0 0 20 20" fill="none" stroke="#cfd9df" stroke-width="1.5"><rect x="2" y="4.5" width="16" height="11" rx="1"/><polyline points="2,5 10,11 18,5"/></svg>
        youremail@website.com
      </p>
    </div>
  </div>
</section>

</body>
</html>
```